Dubai Family protection infographic

We need to produce a way of attracting people to a life insurance and critical illness cover seminar. As this is a pretty dull subject for most people, so we need a cool way of getting people to read the invite/marketing collateral.

We're thinking some kind of colourful and attractive infographic that we can use on flyers and posters as well as online and as an emailer.

Content for the graphic is as bellow:

How much does it cost to replace Mum & Dad?

Mum = Chauffer, Cook, Laundry Service, Household Cleaner, Psychologist, Money Manager

Mums typically work a 94-hour week. At a rather paltry $12 per hour, that’s $4,888 per month – or $58,656 each year. (Source: paywell.net)

Dad : The average Western Expat’s salary in the Gulf is $12,215 per month. That’s $146,580 each year. (Source: Harbor Ledger).

Did you know that the average age of critical illness claimants in the Middle East last year was just 48. Of these, 44% were for cancer while 41% were heart related.

The average age of a death claimant was just 50 years old.
(Source: Lindqvist Mutual Assurance)

1 in 3 people will develop some form of cancer during their lifetime.

That’s 2.36 billion people globally.

And that’s equivalent to the population of China, USA, Brazil, Russia, Philippines, France, UK, South Africa and Italy combined.

Does your family have the resources to hand to cope if a tragedy happens to you?

What can you do to protect them and yourself?

Come to the UAE’s first national protection seminar to find out. Join us at Palmcrest Memorial Sports Ground on June 19th at 19:00.

To pre-register, visit www.brightvane.com/events or alternatively register on the door.

```html
<!DOCTYPE html>
<html lang="en">
<head>
<meta charset="utf-8">
<title>Family Protection Seminar Flyer</title>
<link rel="stylesheet" href="https://fonts.googleapis.com/css2?family=Arimo:wght@400;700&family=Open+Sans:ital,wght@0,400;0,700;1,400;1,700&family=Dancing+Script:wght@700&display=swap">
<style>
  :root {
    --page-bg: #1c1c1c;
    --paper: #ffffff;
    --sky-top: #bfe6f7;
    --sky-mid: #5fb7e0;
    --sea-deep: #1d5f93;
    --sea-mid: #3c8fc6;
    --sand: #7fb6d6;
    --green: #9dbd21;
    --green-light: #b3cf2e;
    --blue: #1f6db2;
    --blue-light: #4a97d6;
    --blue-pale: #8fc0e8;
    --mum-yellow: #f3d22b;
    --arrow-red: #d8231f;
    --ink: #111111;
    --ink-soft: #3a3a3a;
    --link: #1f78c8;
  }
  html, body {
    margin: 0;
    padding: 0;
    width: 1178px;
    height: 1200px;
    overflow: hidden;
    background: var(--page-bg);
  }
  .flyer {
    position: absolute;
    left: 189px;
    top: 32px;
    width: 800px;
    height: 1136px;
    background: var(--paper);
    overflow: hidden;
    font-family: "Open Sans", Arial, sans-serif;
  }
  .hero-photo {
    position: absolute;
    left: 0; top: 0;
    width: 800px; height: 440px;
    background:
      radial-gradient(ellipse 60% 45% at 62% 8%, rgba(255,255,255,0.85), rgba(255,255,255,0) 70%),
      linear-gradient(180deg, var(--sky-top) 0%, var(--sky-mid) 28%, var(--sea-mid) 40%, var(--sea-deep) 60%, var(--sea-mid) 78%, var(--sand) 100%);
  }
  .shapes {
    position: absolute;
    left: 0; top: 0;
    width: 800px; height: 1136px;
  }
  .headline {
    position: absolute;
    left: 0; top: 24px;
    width: 800px;
    margin: 0;
    text-align: center;
    font-family: "Arimo", Arial, sans-serif;
    font-weight: 700;
    font-size: 38px;
    line-height: 52px;
    color: #ffffff;
    text-shadow: 0 2px 3px rgba(0,40,80,0.55);
    letter-spacing: 0.5px;
  }
  .preregister {
    position: absolute;
    left: 26px; top: 335px;
  }
  .preregister-title {
    margin: 0;
    font-family: "Arimo", Arial, sans-serif;
    font-weight: 700;
    font-size: 31px;
    line-height: 38px;
    color: var(--blue);
  }
  .preregister-url {
    margin: 2px 0 0;
    font-family: "Arimo", Arial, sans-serif;
    font-size: 23px;
    color: #ffffff;
  }
  .cost-note {
    position: absolute;
    left: 20px;
    width: 385px;
    margin: 0;
    font-size: 14.5px;
    line-height: 23px;
    color: #ffffff;
  }
  .cost-note.mum { top: 458px; }
  .cost-note.dad { top: 580px; }
  .role-label {
    font-family: "Dancing Script", cursive;
    font-size: 30px;
    color: var(--mum-yellow);
    line-height: 20px;
  }
  .growth-icon {
    position: absolute;
    left: 486px; top: 512px;
    width: 70px; height: 82px;
    background: radial-gradient(circle at 45% 40%, #f2504a, var(--arrow-red) 60%, #8e1411);
    border-radius: 40% 40% 30% 30%;
  }
  .claims-intro {
    position: absolute;
    right: 28px; top: 644px;
    width: 680px;
    margin: 0;
    text-align: right;
    font-family: "Arimo", Arial, sans-serif;
    font-weight: 700;
    font-size: 18px;
    line-height: 27px;
    color: var(--ink);
  }
  .fact-list {
    position: absolute;
    left: 0; top: 748px;
    margin: 0; padding: 0;
    list-style: none;
  }
  .fact-list li {
    position: relative;
    padding-left: 318px;
    width: 750px;
    box-sizing: border-box;
    margin-bottom: 14px;
    font-style: italic;
    font-size: 14.5px;
    line-height: 19px;
    color: var(--ink-soft);
  }
  .tick {
    position: absolute;
    left: 272px; top: 1px;
    width: 16px; height: 16px;
  }
  .call-question {
    position: absolute;
    left: 0; top: 934px;
    width: 800px;
    margin: 0;
    text-align: center;
    font-family: "Open Sans", Arial, sans-serif;
    font-weight: 700;
    font-style: italic;
    font-size: 29px;
    color: var(--ink);
  }
  .invite {
    position: absolute;
    left: 0; top: 990px;
    width: 800px;
    margin: 0;
    text-align: center;
    font-weight: 700;
    font-style: italic;
    font-size: 16.5px;
    line-height: 24px;
    color: var(--ink);
  }
  .register-line {
    position: absolute;
    left: 0; top: 1048px;
    width: 800px;
    margin: 0;
    text-align: center;
    font-weight: 700;
    font-style: italic;
    font-size: 16px;
    color: var(--ink);
  }
  .highlight { color: var(--link); }
</style>
</head>
<body>
  <article class="flyer">
    <div class="hero-photo" role="img" aria-label="Photo of an elderly couple standing together at the water's edge on a beach, sun rays over a blue sea"></div>

    <svg class="shapes" viewBox="0 0 800 1136" aria-hidden="true">
      <polygon points="0,283 210,306 463,376 507,440 0,440" fill="var(--green)"/>
      <polygon points="507,440 800,440 800,518 545,482" fill="var(--green-light)"/>
      <polygon points="0,440 507,440 0,910" fill="var(--blue)"/>
      <polygon points="507,440 0,910 0,1000 540,470" fill="var(--blue-light)"/>
      <polygon points="540,470 0,1000 0,1040" fill="var(--blue-pale)"/>
    </svg>

    <h1 class="headline">How much does it cost to replace<br>Mum &amp; Dad?</h1>

    <div class="preregister">
      <p class="preregister-title">Pre-Register</p>
      <p class="preregister-url">www.brightvane.com/events</p>
    </div>

    <p class="cost-note mum"><span class="role-label">Mum</span> : Chauffer, Cook, Laundry Service, Household Cleaner, Psychologist, Money Manager Mums typically work a 94-hour week. At a rather paltry $12 per hour, that’s $4,888 per month or $58,656 each year.</p>

    <p class="cost-note dad"><span class="role-label">Dad</span> : The average Western Expat’s salary in the Gulf is $12,215 per month. That’s $146,580 each year.</p>

    <div class="growth-icon" role="img" aria-label="Illustration of red arrows pointing upward"></div>

    <p class="claims-intro">Did you know that the average age of critical<br>illness claimants in the Middle East last year was just 48.<br>Of these, 44% were for cancer while 41% were heart related.</p>

    <ul class="fact-list">
      <li><svg class="tick" viewBox="0 0 16 16"><path d="M2 8 L6 12 L14 3" fill="none" stroke="#222" stroke-width="2.4"/></svg>The average age of a death claimant was just 50 years old.</li>
      <li><svg class="tick" viewBox="0 0 16 16"><path d="M2 8 L6 12 L14 3" fill="none" stroke="#222" stroke-width="2.4"/></svg>1 in 3 people will develop some form of cancer during their lifetime.</li>
      <li><svg class="tick" viewBox="0 0 16 16"><path d="M2 8 L6 12 L14 3" fill="none" stroke="#222" stroke-width="2.4"/></svg>That’s 2.36 billion people globally.</li>
      <li><svg class="tick" viewBox="0 0 16 16"><path d="M2 8 L6 12 L14 3" fill="none" stroke="#222" stroke-width="2.4"/></svg>And that’s equivalent to the population of China, USA, Brazil, Russia, Philippines, France, UK, South Africa and Italy combined.</li>
    </ul>

    <p class="call-question">What can you do to protect them and yourself?</p>

    <p class="invite">Come to the UAE’s first national protection seminar to find out.<br>Join us at <span class="highlight">Palmcrest Memorial Sports Ground</span> on <span class="highlight">June 19th</span> at <span class="highlight">19:00</span></p>

    <p class="register-line">To pre-register, visit <span class="highlight">www.brightvane.com/events</span> or alternatively register on the door</p>
  </article>
</body>
</html>
```